A slider bar and icons to be used on the map

#Background
We are currently creating a website for tourists to Japan . Named "Maple Trove," It's a website where users can search for shrines and temples across Japan on the map. We are seeking designs for three icons(shrine icon, temple icon, and representing both shrine and temple icon) and a slider bar to be used on this site's map.
#Requirements
Cool and understandable icons and a slider bar that match the web design.
#Web Design Concept
Attached is a reference document.
#Desired Items
We need four items written below.
-Shrine icon
-Temple icon
-Icon representing both shrines and temples (expressed as a single icon)
-Slider bar
#Regarding the Slider Bar
It has two functions:
-Filter popular shrines and temples.
-Filiter shrines and temples with cool kanji.
We would like it to be able to filter from both the right and the left.
We want to express that moving to the right represents popularity or cool kanji. We'd like to express this on the slider bar as a design.
* reference> https://snaps.vextoro.io/k4TnQw8zLp2HsVbX7
Updates
Need extra days to review
Target Market(s)
Inbound tourists to Japan
Look and feel

```html
<!DOCTYPE html>
<html lang="en">
<head>
<meta charset="utf-8">
<title>Maple Trove – Map Filter Sliders</title>
<link href="https://fonts.googleapis.com/css2?family=Poppins:wght@400&display=swap" rel="stylesheet">
<style>
  :root {
    --bg: #ffffff;
    --frame: #bdbdbd;
    --track: #e3e3e3;
    --knob-border: #a9a9a9;
    --accent: #e61e26;
    --warm: #fdb63a;
    --text: #2b2b2b;
    --caret: #6f6f6f;
  }
  * { box-sizing: border-box; margin: 0; padding: 0; }
  html, body { width: 835px; height: 1200px; overflow: hidden; background: var(--bg); }
  body { position: relative; font-family: "Poppins", sans-serif; }
  .filter-panel {
    position: absolute; left: 131px; width: 572px; height: 87px;
    border: 1px solid var(--frame); background: var(--bg);
  }
  .dropdown {
    position: absolute; left: 11px; top: 43px; width: 112px; height: 31px;
    border: 1px solid var(--frame); border-radius: 3px;
    font-size: 13.5px; color: var(--text); line-height: 29px; padding-left: 9px;
    white-space: nowrap;
  }
  .dropdown::after {
    content: ""; position: absolute; right: 10px; top: 12px;
    border-left: 5px solid transparent; border-right: 5px solid transparent;
    border-top: 7px solid var(--caret);
  }
  .track {
    position: absolute; left: 136px; top: 55px; width: 417px; height: 9px;
    border-radius: 5px; background: var(--track);
  }
  .track-fill {
    position: absolute; left: 0; top: 0; height: 9px; border-radius: 5px 0 0 5px;
    width: calc(var(--pos) - 136px);
    background: linear-gradient(90deg, var(--warm), var(--accent));
  }
  .knob {
    position: absolute; top: 48px; width: 23px; height: 23px; margin-left: -11.5px;
    border-radius: 50%; background: var(--bg); border: 1px solid var(--knob-border);
  }
  .knob-min { left: 147px; }
  .knob-max { left: var(--pos); }
  .level-icon {
    position: absolute; top: 17px; width: 26px; height: 24px; margin-left: -13px;
    fill: var(--accent); overflow: visible;
  }
  .level-icon.min { left: 147px; }
  .level-icon.max { left: var(--pos); }
  .crowd circle, .crowd path { stroke: var(--bg); stroke-width: .9; paint-order: stroke; }
  .defs { position: absolute; width: 0; height: 0; }
</style>
</head>
<body>
<svg class="defs" aria-hidden="true">
  <defs>
    <symbol id="person" viewBox="0 0 20 22">
      <circle cx="10" cy="5.5" r="5.2"/>
      <path d="M1.5 22v-4.5c0-5 3.5-6.8 8.5-6.8s8.5 1.8 8.5 6.8V22z"/>
    </symbol>
    <symbol id="crowd-3" viewBox="0 0 26 24">
      <circle cx="5" cy="4.5" r="3"/><path d="M0.5 15V11.65Q0.5 8.5 5 8.5Q9.5 8.5 9.5 11.65V15Z"/>
      <circle cx="21" cy="4.5" r="3"/><path d="M16.5 15V11.65Q16.5 8.5 21 8.5Q25.5 8.5 25.5 11.65V15Z"/>
      <circle cx="13" cy="9" r="3.6"/><path d="M7.5 23V17.35Q7.5 13.5 13 13.5Q18.5 13.5 18.5 17.35V23Z"/>
    </symbol>
    <symbol id="crowd-4" viewBox="0 0 26 24">
      <circle cx="13" cy="3" r="2.3"/><path d="M9.5 11V8.45Q9.5 6 13 6Q16.5 6 16.5 8.45V11Z"/>
      <circle cx="7" cy="8.5" r="2.5"/><path d="M3 17V14.3Q3 11.5 7 11.5Q11 11.5 11 14.3V17Z"/>
      <circle cx="19" cy="8.5" r="2.5"/><path d="M15 17V14.3Q15 11.5 19 11.5Q23 11.5 23 14.3V17Z"/>
      <circle cx="13" cy="13.5" r="2.8"/><path d="M8.5 23V20.15Q8.5 17 13 17Q17.5 17 17.5 20.15V23Z"/>
    </symbol>
    <symbol id="crowd-6" viewBox="0 0 26 24">
      <circle cx="6" cy="3" r="2.3"/><path d="M2.4 10.5V8.3Q2.4 5.8 6 5.8Q9.6 5.8 9.6 8.3V10.5Z"/>
      <circle cx="13" cy="3" r="2.3"/><path d="M9.4 10.5V8.3Q9.4 5.8 13 5.8Q16.6 5.8 16.6 8.3V10.5Z"/>
      <circle cx="20" cy="3" r="2.3"/><path d="M16.4 10.5V8.3Q16.4 5.8 20 5.8Q23.6 5.8 23.6 8.3V10.5Z"/>
      <circle cx="9.5" cy="8.5" r="2.5"/><path d="M5.5 17V14.3Q5.5 11.5 9.5 11.5Q13.5 11.5 13.5 14.3V17Z"/>
      <circle cx="16.5" cy="8.5" r="2.5"/><path d="M12.5 17V14.3Q12.5 11.5 16.5 11.5Q20.5 11.5 20.5 14.3V17Z"/>
      <circle cx="13" cy="14" r="2.7"/><path d="M8.5 23V20.45Q8.5 17.3 13 17.3Q17.5 17.3 17.5 20.45V23Z"/>
    </symbol>
    <symbol id="crowd-8" viewBox="0 0 26 24">
      <circle cx="8" cy="2.3" r="1.9"/><path d="M5 8.5V6.8Q5 4.7 8 4.7Q11 4.7 11 6.8V8.5Z"/>
      <circle cx="18" cy="2.3" r="1.9"/><path d="M15 8.5V6.8Q15 4.7 18 4.7Q21 4.7 21 6.8V8.5Z"/>
      <circle cx="4" cy="7" r="2"/><path d="M0.8 13.5V11.7Q0.8 9.5 4 9.5Q7.2 9.5 7.2 11.7V13.5Z"/>
      <circle cx="22" cy="7" r="2"/><path d="M18.8 13.5V11.7Q18.8 9.5 22 9.5Q25.2 9.5 25.2 11.7V13.5Z"/>
      <circle cx="13" cy="6.5" r="2"/><path d="M9.8 13V11.2Q9.8 9 13 9Q16.2 9 16.2 11.2V13Z"/>
      <circle cx="8" cy="11.5" r="2"/><path d="M4.8 18V16.2Q4.8 14 8 14Q11.2 14 11.2 16.2V18Z"/>
      <circle cx="18" cy="11.5" r="2"/><path d="M14.8 18V16.2Q14.8 14 18 14Q21.2 14 21.2 16.2V18Z"/>
      <circle cx="13" cy="15.5" r="2.3"/><path d="M9.4 23.5V20.8Q9.4 18.3 13 18.3Q16.6 18.3 16.6 20.8V23.5Z"/>
    </symbol>
    <symbol id="torii-1" viewBox="0 0 26 24">
      <path d="M5 24V2h16v22" fill="none" stroke="currentColor" stroke-width="2.4"/>
    </symbol>
    <symbol id="torii-2" viewBox="0 0 26 24">
      <path d="M5 24V2h16v22M5 6h16" fill="none" stroke="currentColor" stroke-width="2.4"/>
      <path d="M10 2v4M16 2v4" stroke="currentColor" stroke-width="1.6"/>
    </symbol>
    <symbol id="torii-3" viewBox="0 0 26 24">
      <path d="M1 2h24M3 7h20M7 2v22M19 2v22M13 2v5" fill="none" stroke="currentColor" stroke-width="2.4"/>
    </symbol>
    <symbol id="torii-4" viewBox="0 0 26 24">
      <path d="M1 2h24M3 7h20M7 2v21M19 2v21M13 2v5" fill="none" stroke="currentColor" stroke-width="2.4"/>
      <rect x="5" y="20" width="4" height="4"/><rect x="17" y="20" width="4" height="4"/>
    </symbol>
    <symbol id="torii-5" viewBox="0 0 30 24">
      <path d="M0 1q15 3 30 0l-1.5 3q-13.5 2-27 0z"/>
      <path d="M3 8h24M8 4v19M22 4v19M15 4v4" fill="none" stroke="currentColor" stroke-width="2.4"/>
      <rect x="6" y="20" width="4" height="4"/><rect x="20" y="20" width="4" height="4"/>
    </symbol>
  </defs>
</svg>

<!-- Popularity filters -->
<section class="filter-panel" style="top:46px;--pos:227px">
  <div class="dropdown">Popular</div>
  <svg class="level-icon min" viewBox="0 0 26 24"><use href="#person" x="4" y="1" width="18" height="22"/></svg>
  <svg class="level-icon max" viewBox="0 0 32 24" style="width:30px;margin-left:-15px"><use href="#person" x="0" y="1" width="15" height="22"/><use href="#person" x="16" y="1" width="15" height="22"/></svg>
  <div class="track"><div class="track-fill"></div></div>
  <div class="knob knob-min"></div><div class="knob knob-max"></div>
</section>

<section class="filter-panel" style="top:157px;--pos:308px">
  <div class="dropdown">Popular</div>
  <svg class="level-icon min" viewBox="0 0 26 24"><use href="#person" x="4" y="1" width="18" height="22"/></svg>
  <svg class="level-icon max crowd" viewBox="0 0 26 24"><use href="#crowd-3"/></svg>
  <div class="track"><div class="track-fill"></div></div>
  <div class="knob knob-min"></div><div class="knob knob-max"></div>
</section>

<section class="filter-panel" style="top:269px;--pos:389px">
  <div class="dropdown">Popular</div>
  <svg class="level-icon min" viewBox="0 0 26 24"><use href="#person" x="4" y="1" width="18" height="22"/></svg>
  <svg class="level-icon max crowd" viewBox="0 0 26 24"><use href="#crowd-4"/></svg>
  <div class="track"><div class="track-fill"></div></div>
  <div class="knob knob-min"></div><div class="knob knob-max"></div>
</section>

<section class="filter-panel" style="top:383px;--pos:470px">
  <div class="dropdown">Popular</div>
  <svg class="level-icon min" viewBox="0 0 26 24"><use href="#person" x="4" y="1" width="18" height="22"/></svg>
  <svg class="level-icon max crowd" viewBox="0 0 26 24"><use href="#crowd-6"/></svg>
  <div class="track"><div class="track-fill"></div></div>
  <div class="knob knob-min"></div><div class="knob knob-max"></div>
</section>

<section class="filter-panel" style="top:495px;--pos:550px">
  <div class="dropdown">Popular</div>
  <svg class="level-icon min" viewBox="0 0 26 24"><use href="#person" x="4" y="1" width="18" height="22"/></svg>
  <svg class="level-icon max crowd" viewBox="0 0 26 24"><use href="#crowd-8"/></svg>
  <div class="track"><div class="track-fill"></div></div>
  <div class="knob knob-min"></div><div class="knob knob-max"></div>
</section>

<!-- Cool kanji filters -->
<section class="filter-panel" style="top:611px;--pos:227px;color:var(--accent)">
  <div class="dropdown">Cool Kanji</div>
  <svg class="level-icon min"><use href="#torii-1"/></svg>
  <svg class="level-icon max"><use href="#torii-2"/></svg>
  <div class="track"><div class="track-fill"></div></div>
  <div class="knob knob-min"></div><div class="knob knob-max"></div>
</section>

<section class="filter-panel" style="top:722px;--pos:308px;color:var(--accent)">
  <div class="dropdown">Cool Kanji</div>
  <svg class="level-icon min"><use href="#torii-1"/></svg>
  <svg class="level-icon max"><use href="#torii-2"/></svg>
  <div class="track"><div class="track-fill"></div></div>
  <div class="knob knob-min"></div><div class="knob knob-max"></div>
</section>

<section class="filter-panel" style="top:834px;--pos:389px;color:var(--accent)">
  <div class="dropdown">Cool Kanji</div>
  <svg class="level-icon min"><use href="#torii-1"/></svg>
  <svg class="level-icon max"><use href="#torii-3"/></svg>
  <div class="track"><div class="track-fill"></div></div>
  <div class="knob knob-min"></div><div class="knob knob-max"></div>
</section>

<section class="filter-panel" style="top:948px;--pos:470px;color:var(--accent)">
  <div class="dropdown">Cool Kanji</div>
  <svg class="level-icon min"><use href="#torii-1"/></svg>
  <svg class="level-icon max"><use href="#torii-4"/></svg>
  <div class="track"><div class="track-fill"></div></div>
  <div class="knob knob-min"></div><div class="knob knob-max"></div>
</section>

<section class="filter-panel" style="top:1061px;--pos:550px;color:var(--accent)">
  <div class="dropdown">Cool Kanji</div>
  <svg class="level-icon min"><use href="#torii-1"/></svg>
  <svg class="level-icon max" style="width:30px;margin-left:-15px"><use href="#torii-5"/></svg>
  <div class="track"><div class="track-fill"></div></div>
  <div class="knob knob-min"></div><div class="knob knob-max"></div>
</section>
</body>
</html>
```